CREATE A 2 layout and logo ( velunarix )

I need to create 2 layout for my company being a homepage will be like and other client control panel and need to create the logo of the company, my company works with website hosting and sale of dedicated server and VPS cloud the company name and velunarix, I want the site to be very accessible and that is not too flashy

Target Market(s)

website hosting

Industry/Entity Type

It Company

Number of Pages Required

2 page

Font styles to use
Sans Serif

Requirements
Must have
• domain velunarix.example
Nice to have
• banners, login area, login webmail
Should not have
• no preference

```html
<!DOCTYPE html>
<html lang="en">
<head>
<meta charset="utf-8">
<title>Velunarix – Hosting</title>
<link href="https://fonts.googleapis.com/css2?family=Open+Sans:ital,wght@0,300;0,400;0,600;0,700;1,400&display=swap" rel="stylesheet">
<style>
:root{
  --navy:#1b3a7a;
  --navy-deep:#15306a;
  --blue:#1d4ab0;
  --link:#2a56b8;
  --ink:#333;
  --muted:#666;
  --band:#3f3f3f;
  --panel-dark:#333;
  --line:#d9d9d9;
  --white:#fff;
}
*{box-sizing:border-box;margin:0;padding:0}
html,body{width:742px;height:1200px;overflow:hidden;background:var(--white);font-family:"Open Sans",sans-serif;color:var(--ink)}
.page{width:742px;height:1200px;position:relative}

/* header */
.site-header{height:68px;border-top:4px solid var(--navy);position:relative}
.brand{position:absolute;left:50px;top:22px;display:flex;align-items:center;gap:8px;font-size:18px;font-weight:600;color:var(--navy);letter-spacing:.3px}
.brand-mark{width:16px;height:16px;border-radius:50%;background:var(--navy)}
.main-nav{position:absolute;left:0;top:0;width:742px;height:52px}
.main-nav a{position:absolute;top:0;height:52px;font-size:8px;color:var(--ink);text-decoration:none;display:flex;align-items:center;padding-top:12px;white-space:nowrap}
.main-nav a.active{left:242px;width:33px;justify-content:center;background:var(--blue);color:var(--white)}
.nav-products{left:293px}
.nav-about{left:355px}
.nav-support{left:412px}
.nav-programs{left:467px}
.nav-contact{left:525px}
.lang{position:absolute;left:580px;top:28px;width:36px;height:17px;border:1px solid #ccc;font-size:6px;display:flex;align-items:center;padding-left:3px;color:#555}
.lang::after{content:"";position:absolute;right:0;top:0;width:9px;height:15px;background:#ddd}
.btn-login{position:absolute;left:632px;top:28px;width:60px;height:17px;background:var(--blue);color:var(--white);font-size:8px;display:flex;align-items:center;justify-content:center}

/* hero */
.hero{height:218px;position:relative;background:linear-gradient(180deg,#1c2a44 0%,#3f6fb8 55%,#6fa8d8 100%)}
.hero-arrow{position:absolute;top:94px;width:25px;height:28px;background:var(--white);display:flex;align-items:center;justify-content:center}
.hero-arrow.prev{left:0}.hero-arrow.next{right:0}
.hero-caption{height:44px;background:var(--band);color:var(--white);font-size:17px;font-weight:300;letter-spacing:.8px;display:flex;align-items:center;justify-content:center}

/* welcome */
.welcome{height:153px;text-align:center;padding-top:25px}
.welcome h1{font-size:17px;font-weight:400;letter-spacing:.3px}
.welcome p{font-size:7.5px;color:var(--muted);line-height:16px;width:400px;margin:10px auto 0}
.btn-outline{display:inline-flex;align-items:center;justify-content:center;width:86px;height:26px;border:1.5px solid var(--navy);border-radius:2px;color:var(--navy);font-size:8.5px;font-weight:600;text-decoration:none}
.welcome .btn-outline{margin-top:13px}

/* services */
.services{height:277px;background:var(--navy);color:var(--white);text-align:center;padding-top:22px}
.services h2{font-size:17px;font-weight:300;letter-spacing:.5px}
.service-list{display:flex;justify-content:space-between;width:600px;margin:20px auto 0}
.service{width:130px}
.service-icon{width:66px;height:66px;margin:0 auto}
.service h3{font-size:11px;font-weight:300;margin-top:5px;letter-spacing:.2px}
.service p{font-size:7px;line-height:13px;margin-top:8px;color:#dfe6f5}
.btn-small{display:inline-block;margin-top:12px;border:1px solid var(--white);font-size:7px;padding:4px 9px;color:var(--white);text-decoration:none}

/* info */
.info{height:334px;position:relative}
.col{position:absolute;top:30px}
.col-title{font-size:10px;font-weight:400;color:var(--link);padding-bottom:10px;border-bottom:1px solid var(--link)}
.about{left:50px;width:186px}
.about-photo{margin-top:16px;width:186px;height:107px;background:linear-gradient(90deg,#d6d9de,#7b8596)}
.about p{font-size:8px;color:var(--muted);line-height:16.5px;margin-top:15px;width:194px}
.about .btn-outline{margin-top:19px}
.news{left:276px;width:194px}
.news-item{margin-top:16px;border-bottom:1px solid #e3e3e3;padding-bottom:7px}
.news-item + .news-item{margin-top:13px}
.news-row{display:flex;gap:10px}
.news-thumb{width:65px;height:57px;flex:none;background:linear-gradient(135deg,#1d3f7a,#7fb4e0)}
.news-thumb.alt{background:linear-gradient(135deg,#8fb8dc,#2d5a9a)}
.news-row h4{font-size:8px;font-weight:400;color:var(--link)}
.news-row p{font-size:6.5px;color:#555;line-height:15px;margin-top:3px}
.news-meta{display:flex;gap:16px;font-size:6.5px;color:#555;margin-top:9px;padding-left:4px}
.news-meta span{display:flex;align-items:center;gap:4px}
.news .btn-outline{display:flex;margin:12px auto 0}
.login{left:507px;width:185px}
.acc{margin-top:16px;width:184px}
.acc-head{height:36px;display:flex;align-items:center;justify-content:center;position:relative;color:var(--white);font-size:9.5px;font-weight:700;letter-spacing:.3px}
.acc-head.dark{background:var(--panel-dark)}
.acc-head.open{background:var(--navy-deep)}
.acc-head svg{position:absolute;right:12px;top:15px}
.acc-body{background:var(--navy);padding:10px 18px 14px;text-align:center}
.acc-body p{font-size:7px;font-style:italic;color:var(--white);line-height:11px}
.field{height:22px;background:#f2f2f2;margin-top:13px;font-size:7px;color:#888;text-align:left;padding:7px 10px}
.field + .field{margin-top:13px}
.btn-panel{display:inline-flex;width:70px;height:20px;border:1.5px solid var(--white);color:var(--white);font-size:7.5px;font-weight:700;align-items:center;justify-content:center;margin-top:19px}

/* footer */
.site-footer{position:absolute;left:0;top:1094px;width:742px;text-align:center}
.footer-rule{width:372px;height:1px;background:var(--line);margin:0 auto}
.social{display:flex;justify-content:center;gap:13px;margin-top:22px}
.social a{width:31px;height:31px;border:1.5px solid #333;border-radius:50%;display:flex;align-items:center;justify-content:center;font-size:7px;font-weight:600;color:#333;text-decoration:none}
.social a:first-child{border-color:var(--navy);color:var(--navy)}
.copyright{font-size:7.5px;color:#444;margin-top:12px}
</style>
</head>
<body>
<div class="page">
  <header class="site-header">
    <div class="brand"><span class="brand-mark"></span>VELUNARIX</div>
    <nav class="main-nav">
      <a class="active" href="#">Home</a>
      <a class="nav-products" href="#">Products ⌄</a>
      <a class="nav-about" href="#">About Us</a>
      <a class="nav-support" href="#">Support ⌄</a>
      <a class="nav-programs" href="#">Programs</a>
      <a class="nav-contact" href="#">Contact Us</a>
    </nav>
    <div class="lang">En</div>
    <a class="btn-login">Login</a>
  </header>

  <section class="hero" role="img" aria-label="Banner photo of three monitors showing dashboards in front of server racks">
    <span class="hero-arrow prev"><svg width="8" height="10" viewBox="0 0 8 10"><path d="M6 1 2 5l4 4" fill="none" stroke="#1b3a7a" stroke-width="2"/></svg></span>
    <span class="hero-arrow next"><svg width="8" height="10" viewBox="0 0 8 10"><path d="M2 1l4 4-4 4" fill="none" stroke="#1b3a7a" stroke-width="2"/></svg></span>
  </section>
  <div class="hero-caption">POWERFUL AND COST EFFECTIVE HOSTING FOR BUSINESS SOLUTIONS</div>

  <section class="welcome">
    <h1>WELCOME TO VELUNARIX</h1>
    <p>Duis aute irure dolor in reprehenderit in voluptate velit esse cillum dolore eu fugiat nulla pariatur. Excepteur sint occaecat cupidatat non proident, sunt in culpa qui officia deserunt mollit anim id est laborum.</p>
    <a class="btn-outline" href="#">Read More</a>
  </section>

  <section class="services">
    <h2>OUR SERVICES</h2>
    <div class="service-list">
      <div class="service">
        <svg class="service-icon" viewBox="0 0 66 66"><circle cx="33" cy="33" r="31" fill="none" stroke="#fff" stroke-width="2"/><circle cx="33" cy="33" r="14" fill="none" stroke="#fff" stroke-width="1.5"/><ellipse cx="33" cy="33" rx="6" ry="14" fill="none" stroke="#fff" stroke-width="1.5"/><path d="M19 33h28M22 26h22M22 40h22" stroke="#fff" stroke-width="1.5"/></svg>
        <h3>WEB HOSTING</h3>
        <p>Lorem ipsum is the simply dummy text used here for the further purpose usage in the wordpress</p>
        <a class="btn-small" href="#">Learn More</a>
      </div>
      <div class="service">
        <svg class="service-icon" viewBox="0 0 66 66"><circle cx="33" cy="33" r="31" fill="none" stroke="#fff" stroke-width="2"/><rect x="31" y="19" width="16" height="27" fill="#fff"/><path d="M34 24h10M34 29h10M34 34h10M34 39h10" stroke="#1b3a7a" stroke-width="1.5"/><rect x="19" y="32" width="13" height="10" fill="#fff"/><path d="M19 32l6.5 5 6.5-5" fill="none" stroke="#1b3a7a" stroke-width="1.2"/></svg>
        <h3>DEDICATED SERVER</h3>
        <p>Lorem ipsum is the simply dummy text used here for the further purpose usage in the wordpress</p>
        <a class="btn-small" href="#">Learn More</a>
      </div>
      <div class="service">
        <svg class="service-icon" viewBox="0 0 66 66"><circle cx="33" cy="33" r="31" fill="none" stroke="#fff" stroke-width="2"/><path d="M23 30a6 6 0 0 1 5-9 7 7 0 0 1 13 1 5 5 0 0 1 1 9H24z" fill="none" stroke="#fff" stroke-width="1.8"/><rect x="22" y="34" width="6" height="12" fill="#fff"/><rect x="30" y="34" width="6" height="12" fill="#fff"/><rect x="38" y="34" width="6" height="12" fill="#fff"/></svg>
        <h3>VPS CLOUD</h3>
        <p>Lorem ipsum is the simply dummy text used here for the further purpose usage in the wordpress</p>
        <a class="btn-small" href="#">Learn More</a>
      </div>
      <div class="service">
        <svg class="service-icon" viewBox="0 0 66 66"><circle cx="33" cy="33" r="31" fill="none" stroke="#fff" stroke-width="2"/><rect x="19" y="24" width="28" height="19" fill="none" stroke="#fff" stroke-width="2"/><path d="M19 28h28" stroke="#fff" stroke-width="2"/><rect x="23" y="31" width="8" height="8" fill="#fff"/><path d="M34 32h9M34 35h9M34 38h9" stroke="#fff" stroke-width="1.5"/></svg>
        <h3>DOMAIN REGISTRATION</h3>
        <p>Lorem ipsum is the simply dummy text used here for the further purpose usage in the wordpress</p>
        <a class="btn-small" href="#">Learn More</a>
      </div>
    </div>
  </section>

  <section class="info">
    <div class="col about">
      <h2 class="col-title">ABOUT VELUNARIX</h2>
      <div class="about-photo" role="img" aria-label="Photo of a technician standing beside server racks"></div>
      <p>Duis aute irure dolor in reprehenderit in voluptate velit esse cillum dolore eu fugiat nulla pariatur. Excepteur sint occaecat cupidatat non proident, sunt in culpa runt mollit anim id est laborum.</p>
      <a class="btn-outline" href="#">Read More</a>
    </div>

    <div class="col news">
      <h2 class="col-title">LATEST NEWS</h2>
      <article class="news-item">
        <div class="news-row">
          <div class="news-thumb" role="img" aria-label="Photo of a hand holding a glowing city model"></div>
          <div><h4>Lorem ipsum is simply dummy</h4><p>Duis aute irure dolor in reprehender Excepteur sint occaecat cupidatat non runt mollit anim id est laborum.</p></div>
        </div>
        <div class="news-meta"><span>▦ May 06, 2015</span><span>◉ 3 Reviews</span><span>● 10 comments</span></div>
      </article>
      <article class="news-item">
        <div class="news-row">
          <div class="news-thumb alt" role="img" aria-label="Photo of a person with floating digital interface"></div>
          <div><h4>Lorem ipsum is simply dummy</h4><p>Duis aute irure dolor in reprehender Excepteur sint occaecat cupidatat non runt mollit anim id est laborum.</p></div>
        </div>
        <div class="news-meta"><span>▦ May 06, 2015</span><span>◉ 3 Reviews</span><span>● 10 comments</span></div>
      </article>
      <a class="btn-outline" href="#">View All</a>
    </div>

    <div class="col login">
      <h2 class="col-title">LOGIN OPTIONS</h2>
      <div class="acc">
        <div class="acc-head dark">HOSTING LOGIN<svg width="7" height="5" viewBox="0 0 7 5"><path d="M1 1l2.5 2.5L6 1" fill="none" stroke="#fff" stroke-width="1.2"/></svg></div>
        <div class="acc-head open">WEBMAIL LOGIN<svg width="7" height="5" viewBox="0 0 7 5"><path d="M1 4l2.5-2.5L6 4" fill="none" stroke="#fff" stroke-width="1.2"/></svg></div>
        <div class="acc-body">
          <p>Access, manage, and send messages from anywhere in the world.</p>
          <div class="field">Email Address</div>
          <div class="field">Password</div>
          <span class="btn-panel">LOGIN</span>
        </div>
      </div>
    </div>
  </section>

  <footer class="site-footer">
    <div class="footer-rule"></div>
    <div class="social"><a href="#">News</a><a href="#">Talk</a><a href="#">Jobs</a><a href="#">Blog</a></div>
    <p class="copyright">Copyright 2015 - Velunarix. All rights reserved.</p>
  </footer>
</div>
</body>
</html>
```